Chemical Distribution Company Needs a Website

We need a website designed for an existing company based in Michigan. We have grown substantially since inception and we need our website to reflect this growth. It currently has a very mom and pop feel to it. What we do is ship chemicals in Drums, Totes, Bags, Bulk Tank Trucks, and rail from our warehouses in Toledo Oh, and Chicago il. This will be a site that strictly shows what we do and will not be E-commerced based. The final design should communicate a large business with NorthAmerican reach and worldwide sourcing capabilities.

Target Market(s)

What we sell are chemicals such as acids, solvents, oils, and salts all of which are used in the manufacturing process of various products from steel to car parts to paint to car wash soaps to food. We are trying to look like a large company that has stability and track record to go after all types of industries and manufacturers

Industry/Entity Type

It Company

Number of Pages Required

5+ page

Font styles to use
Serif
Sans Serif

Requirements
Must have
• Be Formatted for WIX as that is what we use to Host and Build. Unless you have a better idea. I would also like it to be viewed on a mobile platform which it is not now.
• Tabs for:
• Home Page (similar to "www.brindlemoor.com")
• Who we are- with subtabs for (Overview, Leadership, and Capabilities)
• Chemicals- (subtabs for (overview, Chemicals A-Z) Look at Brindlemoor.com
• Metal Working Lubricants (with a drop down identical to the products tab at "www.veltraslube.com"
• Contact- Very similar to www.quorvanta.com/contact/
• Need to have professional photos of Chemical Facilities, Bulk Tanks Trucks, Chemical Railcars, Storage Facilities filled with Drums and Totes, a Tank Farm.
Nice to have
• Want to have our site look like a combination of quorvanta.com, brindlemoor.com, and plimtoreach.com

```html
<!DOCTYPE html>
<html lang="en">
<head>
<meta charset="utf-8">
<title>Kelvane Chemicals</title>
<link rel="stylesheet" href="https://fonts.googleapis.com/css2?family=Saira:wght@400;500;600;700&family=Lato:wght@400;700&family=Ubuntu:wght@500&display=swap">
<style>
:root{
  --blue:#27a3f0;
  --blue-dark:#0b5a86;
  --navy:#0e3a55;
  --ink:#333a40;
  --muted:#6b7278;
  --light:#f2f3f5;
  --line:#dcdfe3;
  --white:#ffffff;
  --band:rgba(10,70,110,.82);
}
*{margin:0;padding:0;box-sizing:border-box}
html,body{width:1200px;height:2659px;overflow:hidden}
body{position:relative;background:var(--white);font-family:"Lato",sans-serif;color:var(--ink)}
.abs{position:absolute}
.center{text-align:center}

/* header */
.site-header{left:0;top:0;width:1200px;height:113px;background:var(--light)}
.brand{left:58px;top:34px;display:flex;align-items:center;gap:14px}
.brand-dot{width:46px;height:46px;border-radius:50%;background:var(--blue)}
.brand-name{font-family:"Saira",sans-serif;font-weight:700;font-size:34px;color:var(--navy);letter-spacing:.5px}
.contact-item{top:34px;display:flex;gap:16px;align-items:flex-start}
.contact-label{font-size:16px;color:var(--blue);font-weight:700}
.contact-value{font-size:15px;color:var(--muted);margin-top:4px}

.main-nav{left:0;top:113px;width:1200px;height:77px;background:var(--white);border-top:1px solid var(--line);border-bottom:1px solid var(--line)}
.nav-link{top:32px;font-size:14px;color:var(--navy);letter-spacing:.4px;font-weight:700}
.nav-link.active{color:var(--blue)}
.nav-divider{top:27px;width:1px;height:24px;background:var(--line)}
.search-box{left:961px;top:20px;width:159px;height:37px;border:1px solid var(--line);background:var(--white);font-size:11px;color:#aaa;padding:11px 9px}
.search-btn{left:1120px;top:20px;width:37px;height:37px;background:var(--blue)}

/* buttons */
.btn{display:flex;align-items:center;justify-content:center;background:var(--blue);color:var(--white);font-size:13px;font-weight:700;letter-spacing:.5px}
.btn-outline{display:flex;align-items:center;justify-content:center;gap:6px;border:1px solid var(--white);color:var(--white);font-size:12px}
.btn-outline.filled{background:var(--white);color:var(--blue)}

/* hero */
.hero{left:0;top:190px;width:1200px;height:611px;background:linear-gradient(100deg,#3c4650 0%,#6c7884 35%,#5b6470 60%,#2f3740 100%)}
.hero-shade{left:0;top:190px;width:1200px;height:611px;background:rgba(20,28,36,.35)}
.hero-title{left:0;top:340px;width:1200px;font-family:"Saira",sans-serif;font-weight:500;font-size:57px;line-height:66px;color:var(--white);letter-spacing:-.5px}
.hero-text{left:160px;top:486px;width:880px;font-size:13px;line-height:22px;color:var(--white)}
.slider-arrow{width:56px;height:56px;border-radius:50%;background:#e6e8ea;display:flex;align-items:center;justify-content:center}

/* welcome */
.section-title{font-family:"Saira",sans-serif;font-weight:500;font-size:36px;color:var(--blue)}
.section-title .dark{color:var(--navy)}
.body-text{font-size:13px;line-height:23px;color:var(--ink)}

/* who we are */
.who{left:0;top:1078px;width:1200px;height:466px;background:linear-gradient(110deg,#1b4f72 0%,#2f6f95 45%,#1d5678 100%)}
.who-shade{left:0;top:1078px;width:1200px;height:466px;background:rgba(12,72,112,.55)}
.who-title{left:0;top:1110px;width:1200px;font-family:"Saira",sans-serif;font-size:36px;color:var(--white)}
.who-line{left:245px;top:1255px;width:670px;height:2px;background:var(--white)}
.who-icon{width:132px;height:132px;border-radius:50%;background:var(--blue);border:5px solid var(--white);display:flex;align-items:center;justify-content:center}
.who-icon.alt{background:var(--white);border-color:var(--blue)}
.who-card{width:280px;text-align:center;color:var(--white)}
.who-card h3{font-size:16px;font-weight:700;letter-spacing:.4px;margin-bottom:8px}
.who-card p{font-size:12.5px;line-height:18px;color:#d7e6f0}

/* chemicals */
.chem-photo{left:66px;top:1659px;width:306px;height:262px;background:linear-gradient(135deg,#dff2fb 0%,#7fc6ea 50%,#2b8fcc 100%)}
.chem-sub{left:409px;top:1654px;font-family:"Ubuntu",sans-serif;font-weight:500;font-size:23px;color:var(--navy)}
.chem-text{left:413px;top:1703px;width:722px;font-size:13px;line-height:28.5px;color:var(--muted)}

/* lubricants */
.lube{left:0;top:1971px;width:1200px;height:310px;background:linear-gradient(100deg,#173f5a 0%,#356c8c 50%,#1a4a68 100%)}
.lube-shade{left:0;top:1971px;width:1200px;height:310px;background:rgba(12,72,112,.5)}
.lube-title{left:0;top:2010px;width:1200px;font-family:"Saira",sans-serif;font-size:36px;color:var(--white)}
.lube-item{display:flex;align-items:center;gap:14px;font-size:17px;color:var(--white)}

/* footer */
.footer{left:0;top:2281px;width:1200px;height:284px;background:var(--light)}
.footer-brand{left:86px;top:2395px;display:flex;align-items:center;gap:12px}
.footer-brand .mark{width:40px;height:40px;border-radius:50%;background:#2b2b2b}
.footer-brand .name{font-family:"Saira",sans-serif;font-weight:700;font-size:24px;color:#2b2b2b}
.footer-divider{top:2311px;width:1px;height:232px;background:var(--line)}
.footer-col{top:2320px}
.footer-col h4{font-size:17px;font-weight:700;color:var(--navy);margin-bottom:16px}
.footer-col li{list-style:none;font-size:11.5px;color:#8a9096;line-height:28px;padding-left:14px;position:relative}
.footer-col li::before{content:"";position:absolute;left:0;top:13px;width:4px;height:4px;border-radius:50%;background:#b8bdc2}

.bottom-bar{left:0;top:2565px;width:1200px;height:94px;background:var(--blue)}
.copyright{left:0;top:2604px;width:1254px;font-size:12px;color:var(--white);font-weight:700}
.social{top:2598px;width:28px;height:28px;border:2px solid var(--white)}
</style>
</head>
<body>

<header class="abs site-header">
  <div class="abs brand"><span class="brand-dot"></span><span class="brand-name">KELVANE CHEMICALS</span></div>
  <div class="abs contact-item" style="left:650px">
    <svg width="40" height="30" viewBox="0 0 40 30"><rect x="2" y="5" width="34" height="22" rx="2" fill="var(--navy)" transform="rotate(-12 20 16)"/><path d="M5 9 L20 20 L37 5" stroke="#fff" stroke-width="2" fill="none" transform="rotate(-12 20 16)"/></svg>
    <div><div class="contact-label">Email id :</div><div class="contact-value">info@kelvanechem.com</div></div>
  </div>
  <div class="abs contact-item" style="left:1018px">
    <svg width="22" height="26" viewBox="0 0 22 26"><path d="M5 2 L9 7 L7 10 C8 14 11 17 14 18 L17 16 L21 20 L18 24 C9 23 2 15 1 6 Z" fill="var(--navy)"/></svg>
    <div><div class="contact-label">Call Us :</div><div class="contact-value">08 5550 0147</div></div>
  </div>
</header>

<nav class="abs main-nav">
  <span class="abs nav-link active" style="left:73px">HOME</span>
  <span class="abs nav-divider" style="left:156px"></span>
  <span class="abs nav-link" style="left:193px">WHO WE ARE</span>
  <span class="abs nav-divider" style="left:320px"></span>
  <span class="abs nav-link" style="left:365px">CHEMICALS</span>
  <span class="abs nav-divider" style="left:487px"></span>
  <span class="abs nav-link" style="left:523px">METAL WORKING LUBRICANTS</span>
  <span class="abs nav-divider" style="left:780px"></span>
  <span class="abs nav-link" style="left:817px">CONTACT</span>
  <div class="abs search-box">Search</div>
  <div class="abs search-btn"><svg width="37" height="37" viewBox="0 0 37 37"><circle cx="17" cy="17" r="5" stroke="#fff" stroke-width="2" fill="none"/><path d="M21 21 L25 25" stroke="#fff" stroke-width="2"/></svg></div>
</nav>

<section>
  <div class="abs hero" role="img" aria-label="Photo of a bulk tank truck on a highway"></div>
  <div class="abs hero-shade"></div>
  <h1 class="abs hero-title center">LOREM IPSUM DOLOR SIT AMET,<br>CONSECTETUR ADIPISCING ELIT</h1>
  <p class="abs hero-text center">Lorem ipsum dolor sit amet, consectetur adipiscing elit, sed do eiusmod tempor incididunt ut labore et dolore magna aliqua. Ut enim ad minim veniam, quis nostrud exercitation ullamco laboris nisi ut aliquip ex ea commodo consequat. Duis aute irure dolor in reprehenderit in voluptate velit esse cillum dolore eu fugiat nulla pariatur.</p>
  <a class="abs btn" style="left:514px;top:569px;width:131px;height:39px">READ MORE</a>
  <div class="abs slider-arrow" style="left:-9px;top:443px"><svg width="12" height="16" viewBox="0 0 12 16"><path d="M9 2 L3 8 L9 14" stroke="#333" stroke-width="2.5" fill="none"/></svg></div>
  <div class="abs slider-arrow" style="left:1157px;top:443px"><svg width="12" height="16" viewBox="0 0 12 16"><path d="M3 2 L9 8 L3 14" stroke="#333" stroke-width="2.5" fill="none"/></svg></div>
</section>

<section>
  <h2 class="abs section-title center" style="left:0;top:841px;width:1200px">WELCOME TO KELVANE <span class="dark">CHEMICALS</span></h2>
  <p class="abs body-text center" style="left:134px;top:907px;width:932px">Lorem ipsum dolor sit amet, consectetur adipiscing elit, sed do eiusmod tempor incididunt ut labore et dolore magna aliqua. Ut enim ad minim veniam, quis nostrud exercitation ullamco laboris nisi ut aliquip ex ea commodo consequat. Duis aute irure dolor in reprehenderit in voluptate velit esse cillum dolore eu fugiat nulla pariatur. Excepteur sint occaecat cupidatat non proident, sunt in culpa qui officia deserunt mollit anim id est laborum.</p>
  <a class="abs btn" style="left:535px;top:996px;width:140px;height:41px">READ MORE</a>
</section>

<section>
  <div class="abs who" role="img" aria-label="Photo of a fuel hose nozzle at a chemical loading station"></div>
  <div class="abs who-shade"></div>
  <h2 class="abs who-title center">WHO WE ARE</h2>
  <svg class="abs" style="left:52px;top:1320px" width="20" height="18" viewBox="0 0 20 18"><path d="M18 1 L2 9 L18 17 L13 9 Z" fill="#fff"/></svg>
  <svg class="abs" style="left:1138px;top:1320px" width="20" height="18" viewBox="0 0 20 18"><path d="M2 1 L18 9 L2 17 L7 9 Z" fill="#fff"/></svg>
  <div class="abs who-line"></div>

  <div class="abs who-icon alt" style="left:179px;top:1189px">
    <svg width="70" height="70" viewBox="0 0 70 70"><circle cx="32" cy="38" r="24" fill="var(--navy)"/><circle cx="48" cy="22" r="11" fill="#fff" stroke="var(--blue)" stroke-width="4"/><path d="M56 30 L66 40" stroke="var(--blue)" stroke-width="5"/></svg>
  </div>
  <div class="abs who-icon" style="left:530px;top:1189px">
    <svg width="70" height="60" viewBox="0 0 70 60"><circle cx="35" cy="16" r="10" fill="#fff"/><path d="M19 50 C19 34 51 34 51 50 Z" fill="#fff"/><circle cx="14" cy="22" r="7" fill="#fff"/><path d="M2 48 C2 36 20 34 22 40 L18 48 Z" fill="#fff"/><circle cx="56" cy="22" r="7" fill="#fff"/><path d="M68 48 C68 36 50 34 48 40 L52 48 Z" fill="#fff"/></svg>
  </div>
  <div class="abs who-icon" style="left:849px;top:1189px">
    <svg width="70" height="64" viewBox="0 0 70 64"><circle cx="26" cy="38" r="16" fill="none" stroke="#fff" stroke-width="8" stroke-dasharray="6 4"/><circle cx="26" cy="38" r="6" fill="#fff"/><circle cx="52" cy="16" r="10" fill="none" stroke="#fff" stroke-width="6" stroke-dasharray="4 3"/><circle cx="54" cy="48" r="8" fill="none" stroke="#fff" stroke-width="5" stroke-dasharray="3 3"/></svg>
  </div>

  <div class="abs who-card" style="left:110px;top:1343px"><h3>OVERVIEW</h3><p>Lorem ipsum dolor sit amet, consectetur edit adipiscing elit, sed do eiusmod tempor incididunt utdolore magna aliqua.</p></div>
  <div class="abs who-card" style="left:460px;top:1343px"><h3>LEADERSHIP</h3><p>Lorem ipsum dolor sit amet, consectetur edit adipiscing elit, sed do eiusmod tempor incididunt utdolore magna aliqua.</p></div>
  <div class="abs who-card" style="left:775px;top:1343px"><h3>CAPABILITIES</h3><p>Lorem ipsum dolor sit amet, consectetur edit adipiscing elit, sed do eiusmod tempor incididunt utdolore a aliqua.</p></div>

  <a class="abs btn-outline filled" style="left:210px;top:1437px;width:83px;height:31px">More <svg width="6" height="8" viewBox="0 0 6 8"><path d="M0 0 L6 4 L0 8Z" fill="var(--blue)"/></svg></a>
  <a class="abs btn-outline" style="left:564px;top:1437px;width:83px;height:31px">More <svg width="6" height="8" viewBox="0 0 6 8"><path d="M0 0 L6 4 L0 8Z" fill="#fff"/></svg></a>
  <a class="abs btn-outline" style="left:898px;top:1437px;width:83px;height:31px">More <svg width="6" height="8" viewBox="0 0 6 8"><path d="M0 0 L6 4 L0 8Z" fill="#fff"/></svg></a>
</section>

<section>
  <h2 class="abs section-title center" style="left:0;top:1574px;width:1200px">CHEMICALS</h2>
  <div class="abs chem-photo" role="img" aria-label="Photo of laboratory glass flasks and a molecule model in blue light"></div>
  <h3 class="abs chem-sub">Commodity, Specialty and Custom formulas</h3>
  <p class="abs chem-text">Lorem ipsum dolor sit amet, consectetur adipiscing elit, sed do eiusmod tempor incididunt ut labore et dolore magna aliqua. Ut enim ad minim veniam, quis nostrud exercitation ullamco laboris nisi ut aliquip ex ea commodo consequat. Duis aute irure dolor in reprehenderit in voluptate velit esse cillum dolore eu fugiat nulla pariatur. Excepteur sint occaecat cupidatat non proident, sunt in culpa qui officia deserunt mollit anim id est laborum. Laboris nisi ut aliquip ex ea commodo consequat. Duis aute irure dolor in reprehenderit in voluptate velit esse cillum dolore eu fugiat nulla pariatur. Excepteur sint occaecat cupidatat non proident, sunt in culpa qui officia deserunt mollit anim id est laborum.</p>
  <a class="abs btn" style="left:413px;top:1886px;width:129px;height:35px">READ MORE</a>
</section>

<section>
  <div class="abs lube" role="img" aria-label="Photo of a metal machining tool with coolant spray"></div>
  <div class="abs lube-shade"></div>
  <h2 class="abs lube-title center">METAL WORKING LUBRICANTS</h2>
  <div class="abs lube-item" style="left:166px;top:2111px"><svg width="16" height="13" viewBox="0 0 16 13"><path d="M1 7 L6 11 L15 1" stroke="var(--blue)" stroke-width="3" fill="none"/></svg>Vanishing</div>
  <div class="abs lube-item" style="left:166px;top:2151px"><svg width="16" height="13" viewBox="0 0 16 13"><path d="M1 7 L6 11 L15 1" stroke="var(--blue)" stroke-width="3" fill="none"/></svg>Machining &amp; Cutting</div>
  <div class="abs lube-item" style="left:166px;top:2191px"><svg width="16" height="13" viewBox="0 0 16 13"><path d="M1 7 L6 11 L15 1" stroke="var(--blue)" stroke-width="3" fill="none"/></svg>Honing</div>
  <div class="abs lube-item" style="left:485px;top:2108px"><svg width="16" height="13" viewBox="0 0 16 13"><path d="M1 7 L6 11 L15 1" stroke="var(--blue)" stroke-width="3" fill="none"/></svg>Gun Drill</div>
  <div class="abs lube-item" style="left:485px;top:2148px"><svg width="16" height="13" viewBox="0 0 16 13"><path d="M1 7 L6 11 L15 1" stroke="var(--blue)" stroke-width="3" fill="none"/></svg>Grinding</div>
  <div class="abs lube-item" style="left:485px;top:2188px"><svg width="16" height="13" viewBox="0 0 16 13"><path d="M1 7 L6 11 L15 1" stroke="var(--blue)" stroke-width="3" fill="none"/></svg>Extrusion &amp; Cold Heading</div>
  <div class="abs lube-item" style="left:812px;top:2108px"><svg width="16" height="13" viewBox="0 0 16 13"><path d="M1 7 L6 11 L15 1" stroke="var(--blue)" stroke-width="3" fill="none"/></svg>Drawing &amp; Stamping</div>
  <div class="abs lube-item" style="left:812px;top:2148px"><svg width="16" height="13" viewBox="0 0 16 13"><path d="M1 7 L6 11 L15 1" stroke="var(--blue)" stroke-width="3" fill="none"/></svg>Transmission oils</div>
  <div class="abs lube-item" style="left:812px;top:2188px"><svg width="16" height="13" viewBox="0 0 16 13"><path d="M1 7 L6 11 L15 1" stroke="var(--blue)" stroke-width="3" fill="none"/></svg>Tractor oils</div>
</section>

<footer>
  <div class="abs footer"></div>
  <div class="abs footer-brand"><span class="mark"></span><span class="name">KELVANE</span></div>
  <span class="abs footer-divider" style="left:376px"></span>
  <span class="abs footer-divider" style="left:656px"></span>
  <span class="abs footer-divider" style="left:938px"></span>
  <div class="abs footer-col" style="left:408px"><h4>Important Links</h4><ul><li>Affiliate Program</li><li>Special Promotions</li><li>Newsletter</li><li>Contact</li></ul></div>
  <div class="abs footer-col" style="left:690px"><h4>Categories</h4><ul><li>Overview</li><li>Leadership</li><li>Capabilities</li><li>Chemicals</li></ul></div>
  <div class="abs footer-col" style="left:973px"><h4>Navigation</h4><ul><li>About Us</li><li>Who we are</li><li>News</li><li>Metal Working Lubricant</li><li>Contact Us</li></ul></div>

  <div class="abs bottom-bar"></div>
  <p class="abs copyright center">Copyright 2015 Company Name.&nbsp; All Rights Reserved.</p>
  <span class="abs social" style="left:1040px"></span>
  <span class="abs social" style="left:1084px"></span>
  <span class="abs social" style="left:1126px"></span>
</footer>

</body>
</html>
```